New launch of custom scented perfume and gifts and products for bridal and gift industry.

We create personalized aromatherapy blends, natural essence perfumes and scented gifts for individuals and special events. This Product Label is for general use, but specifically, this product is called Velora Mist, I would like the ingredients to be on the back in vertical print, have the oz/ml and the words custom-blended in Colorado on the label front and center. I am seeking a unique and colorful label that is elegant but modern. I am looking to set my brand apart from the minimalistic look that is very popular right now. I am open to use of foil or metallics in discreet ways in the label design. I want something that I can use as a general brand direction for my current bottles and then something that can be slightly altered (rectangle - square for instance) if or when the bottle shape changes from cylinder. I can use either clear or white background. Since it's a small bottle, it's important to have the logo, name of product, custom-blended in Colorado and the oz/ml centered so it doesn't wrap too far around the bottle. The size of the initial label is 2.75 wide x 1.5 high. I envision having the ability to resize the label design as I my product line grows. The ingredients, precautions and web address can be written with the text turned vertical to save space. My Website is quenmora-scents.example. Please see my site for the design esthetic as I'd like to compliment that. Attached is my new logo as well!

Project Deadline Extended Reason: I have just received some new versions and new designs that I really like and would like to extend my contest to give designers time to review. I am also going to guarantee this contest so you all know I am serious about choosing the right design.Thank you again for your efforts, I look forward to seeing other submissions. Added Thursday, September 28, 2017

Target are men, women and holistic practitioners who care about and are invested in luxury and bespoke naturally sourced body care products and natural essence perfumes. Income average, $80,000 - $250,000 +

Cosmetics

Serif
Sans Serif
Decorative
Script

• Ysël Drops Logo/ or the words Ysël Drops
• 1 oz/ 30ml
• name of product: Velora Mist #4
• Custom-Blended in Colorado
• www.quenmora-scents.example
• KEEP OUT OF CHILDREN'S REACH KEEP CLEAR OF EYES/SENSITIVE SKIN. EXTERNAL USE ONLY
• Colorful, elegant, pastels, maybe a touch of metallic, cursive font for the words Velora Mist.
• Please, no more lotus!

```html
<!DOCTYPE html>
<html lang="en">
<head>
<meta charset="utf-8">
<title>Ysël Drops — Velora Mist label options</title>
<link href="https://fonts.googleapis.com/css2?family=Amatic+SC:wght@400;700&family=Raleway:wght@300;400&display=swap" rel="stylesheet">
<style>
  :root {
    --page: #ffffff;
    --label-cream: #f8f8da;
    --cut-line: #ec8a7c;
    --safe-line: #9ccbd9;
    --brand-brown: #9a6a45;
    --tag-brown: #6a3c1a;
    --title-top: #c2601c;
    --title-bottom: #6e2a0c;
    --rule: #c9a98a;
    --orn-gold: #e6c9a2;
    --orn-mint: #bfe3d3;
    --orn-lilac: #d9cfe0;
    --orn-peach: #f2d7c6;
    --sw-crimson: #8b1624;
    --sw-coral: #e06a72;
    --sw-lavender: #b9a6d0;
    --sw-indigo: #3c2680;
    --sw-turquoise: #33b9c1;
    --sw-teal: #189682;
    --sw-forest: #145a2c;
    --sw-seafoam: #b3d9cc;
  }
  * { margin: 0; padding: 0; box-sizing: border-box; }
  html, body { width: 1200px; height: 1000px; overflow: hidden; background: var(--page); }
  .sheet { position: relative; width: 1200px; height: 1000px; }

  .label {
    position: absolute; left: 75px; width: 1043px; height: 348px;
    background: var(--label-cream);
    border: 1px solid var(--cut-line); border-radius: 14px;
    overflow: hidden;
  }
  .label--sans { top: 42px; }
  .label--hand { top: 450px; }

  .label__safe {
    position: absolute; inset: 8px;
    border: 1px dashed var(--safe-line); border-radius: 10px;
    z-index: 3; pointer-events: none;
  }
  .label__ornament {
    position: absolute; left: 0; right: 0; bottom: 0; height: 145px;
    background:
      radial-gradient(ellipse 18% 60% at 10% 55%, var(--orn-lilac), transparent 70%),
      radial-gradient(ellipse 14% 50% at 24% 35%, var(--orn-mint), transparent 70%),
      radial-gradient(ellipse 14% 50% at 80% 35%, var(--orn-mint), transparent 70%),
      radial-gradient(ellipse 16% 55% at 92% 40%, var(--orn-peach), transparent 70%),
      radial-gradient(ellipse 30% 70% at 50% 85%, var(--orn-lilac), transparent 70%),
      linear-gradient(to bottom, rgba(230,201,162,0) 0%, var(--orn-gold) 100%);
    z-index: 1;
  }

  .label__brand {
    position: absolute; top: 28px; left: 0; right: 0; text-align: center;
    font-family: "Raleway", sans-serif; font-weight: 400; font-size: 30px;
    line-height: 38px; letter-spacing: 2px; color: var(--brand-brown);
    z-index: 2;
  }
  .label__rule {
    position: absolute; left: 168px; width: 707px; height: 1px;
    background: linear-gradient(to right, transparent, var(--rule) 15%, var(--rule) 85%, transparent);
    z-index: 2;
  }
  .label__rule--top { top: 74px; }
  .label__rule--bottom { top: 197px; }

  .label__title {
    position: absolute; left: 0; right: 0; text-align: center;
    background: linear-gradient(to bottom, var(--title-top), var(--title-bottom));
    -webkit-background-clip: text; background-clip: text; color: transparent;
    white-space: nowrap; z-index: 2;
  }
  .label--sans .label__title {
    top: 78px; font-family: "Raleway", sans-serif; font-weight: 300;
    font-size: 98px; line-height: 116px;
  }
  .label--hand .label__title {
    top: 72px; font-family: "Amatic SC", cursive; font-weight: 400;
    font-size: 122px; line-height: 126px; letter-spacing: 3px;
  }

  .label__tagline {
    position: absolute; top: 210px; left: 0; right: 0; text-align: center;
    font-family: "Amatic SC", cursive; font-weight: 700; font-size: 23px;
    line-height: 30px; color: var(--tag-brown); z-index: 2;
  }

  .palette { position: absolute; left: 0; top: 860px; width: 1200px; height: 140px; display: flex; }
  .palette__swatch { flex: 1; }
  .palette__swatch--crimson { background: var(--sw-crimson); }
  .palette__swatch--coral { background: var(--sw-coral); }
  .palette__swatch--lavender { background: var(--sw-lavender); }
  .palette__swatch--indigo { background: var(--sw-indigo); }
  .palette__swatch--turquoise { background: var(--sw-turquoise); }
  .palette__swatch--teal { background: var(--sw-teal); }
  .palette__swatch--forest { background: var(--sw-forest); }
  .palette__swatch--seafoam { background: var(--sw-seafoam); }
</style>
</head>
<body>
<main class="sheet">
  <section class="label label--sans">
    <div class="label__ornament" role="img" aria-label="Watercolour splashes with gold line-art mandala flourishes along the bottom edge"></div>
    <p class="label__brand">Ysël Drops</p>
    <div class="label__rule label__rule--top"></div>
    <h1 class="label__title">Velora Mist</h1>
    <div class="label__rule label__rule--bottom"></div>
    <p class="label__tagline">Custom-Blended in Colorado</p>
    <div class="label__safe"></div>
  </section>

  <section class="label label--hand">
    <div class="label__ornament" role="img" aria-label="Watercolour splashes with gold line-art mandala flourishes along the bottom edge"></div>
    <p class="label__brand">Ysël Drops</p>
    <div class="label__rule label__rule--top"></div>
    <h2 class="label__title">Velora Mist</h2>
    <div class="label__rule label__rule--bottom"></div>
    <p class="label__tagline">Custom-Blended in Colorado</p>
    <div class="label__safe"></div>
  </section>

  <div class="palette" aria-label="Colour palette">
    <div class="palette__swatch palette__swatch--crimson"></div>
    <div class="palette__swatch palette__swatch--coral"></div>
    <div class="palette__swatch palette__swatch--lavender"></div>
    <div class="palette__swatch palette__swatch--indigo"></div>
    <div class="palette__swatch palette__swatch--turquoise"></div>
    <div class="palette__swatch palette__swatch--teal"></div>
    <div class="palette__swatch palette__swatch--forest"></div>
    <div class="palette__swatch palette__swatch--seafoam"></div>
  </div>
</main>
</body>
</html>
```